Brindle Ecommerce Website Design - Korvel & Pelstry Growth *

The goal of this website is to show case studies and testimonials for Brindle Ecommerce. Our company specializes in Korvel and Pelstry management and growth. The design should communicate trust, growth, and attention to detail.

Below are 3 leading websites in the space
https://quillbrookpartners.com/solutions
https://dorvanstudio.com/
https://velmora.com/

Target Market(s)

Businesses looking to grow on Korvel. Small and large businesses are our clients. Many are brands that are household names.

Industry/Entity Type

Ecommerce

Number of Pages Required

5+ page

Font styles to use
Serif
Sans Serif

```html
<!DOCTYPE html>
<html lang="en">
<head>
<meta charset="utf-8">
<title>Brindle Ecommerce</title>
<link rel="stylesheet" href="https://fonts.googleapis.com/css2?family=Roboto:wght@400;500;700&family=Roboto+Slab:wght@600;700&display=swap">
<style>
:root{
  --purple:#7b1d5e;
  --purple-dark:#5e1547;
  --ink:#1f1f1f;
  --text:#555;
  --light:#f3f3f3;
  --dark:#141416;
  --white:#fff;
}
*{margin:0;padding:0;box-sizing:border-box}
html,body{width:1200px;height:4600px;overflow:hidden}
body{font-family:"Roboto",Arial,sans-serif;color:var(--ink);background:var(--white);position:relative}
.abs{position:absolute}
h2.section-title{font-family:"Roboto Slab",Georgia,serif;font-weight:700;font-size:36px;text-align:center;text-transform:uppercase;color:var(--ink)}
h2.section-title::after{content:"";display:block;width:56px;height:3px;background:var(--ink);margin:12px auto 0}

/* hero */
.hero{left:0;top:0;width:1200px;height:660px;background:radial-gradient(ellipse at 70% 40%,#4a3d3a 0%,#2a2322 45%,#151213 100%)}
.nav{left:0;top:0;width:1200px;height:100px}
.brand{left:30px;top:26px;display:flex;align-items:center;gap:12px;color:var(--white);font-weight:700;font-size:17px;line-height:20px}
.brand-dot{width:30px;height:30px;border-radius:50%;background:var(--purple)}
.nav-links{right:150px;top:42px;display:flex;gap:46px;font-size:15px;color:var(--white)}
.nav-links span:first-child{border-bottom:2px solid var(--white);padding-bottom:4px}
.talk{right:30px;top:32px;background:var(--purple);color:var(--white);font-size:15px;padding:9px 20px}
.hero h1{left:220px;top:240px;width:620px;color:var(--white);font-weight:700;font-size:38px;line-height:52px;text-transform:uppercase;letter-spacing:.5px}
.hero-btn{left:220px;top:398px;border:2px solid var(--purple);color:#c9a3bd;font-size:14px;padding:12px 26px;letter-spacing:1px}
.slider-dot{right:14px;width:8px;height:8px;border-radius:50%;background:#bbb}

/* stats */
.stats{left:0;top:660px;width:1200px;height:190px;display:flex;justify-content:space-between;padding:60px 200px 0 230px}
.stat-num{font-family:"Roboto Slab",Georgia,serif;font-weight:700;font-size:40px;color:var(--purple)}
.stat-label{font-size:12px;color:var(--text);text-transform:uppercase;margin-top:6px}

/* about */
.about{left:0;top:850px;width:1200px;height:530px;background:var(--light)}
.about-photo{left:0;top:0;width:580px;height:530px;background:linear-gradient(135deg,#9b8f88,#cfc5bd 45%,#6f6560)}
.about-copy{left:612px;top:100px;width:470px}
.about-copy h2{font-family:"Roboto Slab",Georgia,serif;font-size:36px;font-weight:700}
.about-copy h2::after{content:"";display:block;width:56px;height:3px;background:var(--ink);margin-top:10px}
.about-lead{font-weight:700;font-size:16px;line-height:24px;margin:22px 0 18px}
.about-copy p{font-size:13px;line-height:21px;color:var(--text);margin-bottom:16px}
.btn-outline{display:inline-block;border:1.5px solid var(--ink);font-size:13px;padding:8px 18px;margin-top:8px}

/* services */
.services-title{left:0;top:1470px;width:1200px}
.service{width:320px;height:328px}
.service-photo{width:320px;height:220px}
.service-label{position:absolute;left:0;top:188px;width:280px;height:140px;background:var(--white);display:flex;align-items:center;gap:18px;padding-left:14px;box-shadow:0 8px 24px rgba(0,0,0,.06)}
.service-icon{width:64px;height:64px;display:flex;align-items:center;justify-content:center;flex:none}
.service-icon.active{background:var(--purple)}
.service-name{font-weight:700;font-size:15px;line-height:20px;text-transform:uppercase}

/* case studies */
.cases-title{left:0;top:2370px;width:1200px}
.case{width:400px;height:352px}
.case-caption{position:absolute;left:0;bottom:0;width:300px;height:68px;background:var(--white);font-weight:700;font-size:13px;line-height:18px;padding:16px 18px;text-transform:uppercase}
.case-arrow{position:absolute;left:300px;bottom:0;width:60px;height:68px;background:#e6e6e6;display:flex;align-items:center;justify-content:center}
.case-arrow.active{background:var(--purple)}

/* testimonials */
.testi-title{left:0;top:3270px;width:1200px}
.quote-badge{left:570px;top:3380px;width:60px;height:60px;border-radius:50%;background:#f4e8f0;display:flex;align-items:center;justify-content:center}
.testi-text{left:270px;top:3468px;width:660px;text-align:center;font-size:14px;line-height:22px;color:var(--text)}
.testi-meta{left:0;top:3550px;width:1200px;display:flex;justify-content:center;gap:40px;font-size:13px;color:var(--text)}
.testi-dots{left:0;top:3630px;width:1200px;display:flex;justify-content:center;gap:12px;align-items:center}
.testi-dots span{width:8px;height:8px;border-radius:50%;background:#ccc}
.testi-dots span.on{width:12px;height:12px;border:2px solid var(--purple);background:var(--white)}

/* form */
.form-band{left:0;top:3740px;width:1200px;height:420px;background:linear-gradient(180deg,#1b1b1e,#0f0f11)}
.form-title{left:0;top:3820px;width:1200px;color:var(--white)}
.form-title::after{background:var(--white)!important}
.field{left:280px;width:300px;height:30px;background:var(--white);font-size:12px;color:#999;padding:8px 12px 0 30px}
.field svg{position:absolute;left:10px;top:9px}
.message{left:600px;top:3896px;width:320px;height:130px;background:var(--white);font-size:12px;color:#999;padding:8px 12px}
.submit{left:548px;top:4060px;width:104px;height:30px;border:1.5px solid var(--white);color:var(--white);font-size:12px;display:flex;align-items:center;justify-content:center;letter-spacing:1px}

/* footer */
.footer{left:0;top:4160px;width:1200px;height:400px;background:var(--white)}
.foot-col{top:50px}
.foot-col h4{font-weight:700;font-size:17px;color:var(--purple)}
.foot-col h4::after{content:"";display:block;width:34px;height:2px;background:var(--purple);margin-top:6px}
.foot-label{font-size:11px;font-weight:700;color:var(--purple);margin-top:18px}
.foot-line{font-size:12px;color:var(--text);line-height:19px;margin-top:4px;display:flex;gap:6px;align-items:center}
.socials{display:flex;gap:10px;margin-top:18px}
.socials span{width:22px;height:22px;border-radius:50%;border:1.5px solid var(--purple)}
.quick{font-size:13px;color:var(--text);line-height:24px;margin-top:16px}
.map{left:600px;top:0;width:600px;height:400px;background:linear-gradient(135deg,#e4e4e4,#d2d2d2)}
.copyright{left:0;top:4560px;width:1200px;height:40px;background:var(--purple);color:var(--white);font-size:12px;display:flex;align-items:center;justify-content:center}
</style>
</head>
<body>

<section class="abs hero" role="img" aria-label="Dark photo of a desk with business charts, laptop and papers"></section>
<header class="abs nav">
  <div class="abs brand"><span class="brand-dot"></span><span>Brindle<br>Ecommerce</span></div>
  <nav class="abs nav-links"><span>About Us</span><span>Services</span><span>Contact Us</span></nav>
  <div class="abs talk">Let's Talk</div>
</header>
<h1 class="abs" style="left:220px;top:240px;width:620px;color:#fff;font-weight:700;font-size:38px;line-height:52px;text-transform:uppercase">Lorem Ipsum is simply dummy text of the printing industry.</h1>
<div class="abs hero-btn">GET STARTED NOW</div>
<span class="abs slider-dot" style="top:276px"></span>
<span class="abs slider-dot" style="top:356px"></span>

<section class="abs stats">
  <div><div class="stat-num">1,248%</div><div class="stat-label">Avg profit increase</div></div>
  <div><div class="stat-num">17</div><div class="stat-label">Awards received</div></div>
  <div><div class="stat-num">$373<span style="font-size:22px">M</span></div><div class="stat-label">Annual revenue managed</div></div>
  <div><div class="stat-num">47</div><div class="stat-label">Certifications</div></div>
</section>

<section class="abs about">
  <div class="abs about-photo" role="img" aria-label="Photo of a team working together at a computer"></div>
  <div class="abs about-copy">
    <h2>ABOUT US</h2>
    <div class="about-lead">Lorem Ipsum is simply dummy text of the printing and typesetting industry</div>
    <p>Lorem Ipsum has been the industry's standard dummy text ever since the 1500s, when an unknown printer took a galley of type and scrambled it to make a type specimen book.</p>
    <p>It has survived not only five centuries, but also the leap into electronic typesetting, remaining essentially unchanged.</p>
    <span class="btn-outline">READ MORE</span>
  </div>
</section>

<h2 class="abs section-title services-title">Services</h2>

<div class="abs service" style="left:100px;top:1560px">
  <div class="service-photo" role="img" aria-label="Photo of colleagues meeting at a desk" style="background:linear-gradient(135deg,#3b3431,#6e625b)"></div>
  <div class="service-label"><div class="service-icon"><svg width="40" height="40" viewBox="0 0 40 40" fill="none" stroke="#333" stroke-width="2"><circle cx="20" cy="10" r="4"/><circle cx="8" cy="30" r="4"/><circle cx="32" cy="30" r="4"/><path d="M20 14v8M20 22L10 27M20 22l10 5"/></svg></div><div class="service-name">Strategic Growth<br>Planning</div></div>
</div>
<div class="abs service" style="left:440px;top:1560px">
  <div class="service-photo" role="img" aria-label="Photo of a man in a warehouse aisle" style="background:linear-gradient(135deg,#8e98a6,#c9b9a0 50%,#5c6470)"></div>
  <div class="service-label"><div class="service-icon active"><svg width="40" height="40" viewBox="0 0 40 40" fill="none" stroke="#fff" stroke-width="2"><rect x="6" y="8" width="28" height="24"/><path d="M6 15h28M12 22h10M12 27h14"/></svg></div><div class="service-name">Product Listing<br>Optimization</div></div>
</div>
<div class="abs service" style="left:780px;top:1560px">
  <div class="service-photo" role="img" aria-label="Photo of notes and charts about paid advertising" style="background:linear-gradient(135deg,#d8d2c4,#a9b4a0 50%,#7f8a92)"></div>
  <div class="service-label"><div class="service-icon"><svg width="40" height="40" viewBox="0 0 40 40" fill="none" stroke="#333" stroke-width="2"><path d="M8 6h18l6 6v22H8z"/><path d="M14 18h12M14 24h12M14 30h8"/></svg></div><div class="service-name">Paid Advertising</div></div>
</div>
<div class="abs service" style="left:100px;top:1912px">
  <div class="service-photo" role="img" aria-label="Photo of hands typing on a laptop" style="background:linear-gradient(135deg,#5b5552,#8b8580)"></div>
  <div class="service-label"><div class="service-icon"><svg width="40" height="40" viewBox="0 0 40 40" fill="none" stroke="#333" stroke-width="2"><circle cx="20" cy="12" r="5"/><path d="M8 32c0-7 5-11 12-11s12 4 12 11z"/></svg></div><div class="service-name">Organic Ranking<br>Services</div></div>
</div>
<div class="abs service" style="left:440px;top:1912px">
  <div class="service-photo" role="img" aria-label="Photo of a city building" style="background:linear-gradient(135deg,#b9a994,#8f7d6c 50%,#6b5e55)"></div>
  <div class="service-label"><div class="service-icon"><svg width="40" height="40" viewBox="0 0 40 40" fill="none" stroke="#333" stroke-width="2"><rect x="6" y="10" width="28" height="22"/><path d="M12 26l6-6 4 4 8-8"/></svg></div><div class="service-name">Product Launch<br>Services</div></div>
</div>
<div class="abs service" style="left:780px;top:1912px">
  <div class="service-photo" role="img" aria-label="Photo of a hand touching a glowing digital network" style="background:linear-gradient(135deg,#1f3d5c,#3d7aa8 50%,#1a2a40)"></div>
  <div class="service-label"><div class="service-icon"><svg width="40" height="40" viewBox="0 0 40 40" fill="none" stroke="#333" stroke-width="2"><path d="M20 6l10 12-10 16-10-16z"/><path d="M10 18h20"/></svg></div><div class="service-name">External Traffic<br>Strategies</div></div>
</div>

<h2 class="abs section-title cases-title">Our Case Studies</h2>

<div class="abs case" style="left:0;top:2468px;background:linear-gradient(135deg,#1c1c1e,#3a3a3d)" role="img" aria-label="Photo of dark cosmetic bottles">
  <div class="case-caption">Lorem Ipsum is simply dummy text of the printing industry</div><div class="case-arrow"><svg width="14" height="14" viewBox="0 0 14 14"><path d="M4 2l6 5-6 5" fill="none" stroke="#333" stroke-width="2"/></svg></div>
</div>
<div class="abs case" style="left:400px;top:2468px;background:linear-gradient(135deg,#b8836a,#e0b79c 50%,#8a5a45)" role="img" aria-label="Photo of a skincare product bottle">
  <div class="case-caption">Lorem Ipsum is simply dummy text of the printing industry</div><div class="case-arrow"><svg width="14" height="14" viewBox="0 0 14 14"><path d="M4 2l6 5-6 5" fill="none" stroke="#333" stroke-width="2"/></svg></div>
</div>
<div class="abs case" style="left:800px;top:2468px;background:linear-gradient(135deg,#6d6a68,#2c2a2a 60%,#4a4846)" role="img" aria-label="Photo of a dark SUV">
  <div class="case-caption">Lorem Ipsum is simply dummy text of the printing industry</div><div class="case-arrow active"><svg width="14" height="14" viewBox="0 0 14 14"><path d="M4 2l6 5-6 5" fill="none" stroke="#fff" stroke-width="2"/></svg></div>
</div>
<div class="abs case" style="left:0;top:2840px;background:linear-gradient(135deg,#4a4a4c,#8c8a86 50%,#2e2e30)" role="img" aria-label="Photo of a wristwatch">
  <div class="case-caption">Lorem Ipsum is simply dummy text of the printing industry</div><div class="case-arrow"><svg width="14" height="14" viewBox="0 0 14 14"><path d="M4 2l6 5-6 5" fill="none" stroke="#333" stroke-width="2"/></svg></div>
</div>
<div class="abs case" style="left:400px;top:2840px;background:linear-gradient(135deg,#c9a46b,#f0d9a8 50%,#8f6d3e)" role="img" aria-label="Photo of a gold cosmetic jar">
  <div class="case-caption">Lorem Ipsum is simply dummy text of the printing industry</div><div class="case-arrow"><svg width="14" height="14" viewBox="0 0 14 14"><path d="M4 2l6 5-6 5" fill="none" stroke="#333" stroke-width="2"/></svg></div>
</div>
<div class="abs case" style="left:800px;top:2840px;background:linear-gradient(135deg,#6b5548,#a38b78 50%,#3e322b)" role="img" aria-label="Photo of a leather bag">
  <div class="case-caption">Lorem Ipsum is simply dummy text of the printing industry</div><div class="case-arrow"><svg width="14" height="14" viewBox="0 0 14 14"><path d="M4 2l6 5-6 5" fill="none" stroke="#333" stroke-width="2"/></svg></div>
</div>

<h2 class="abs section-title testi-title">Testimonials</h2>
<div class="abs quote-badge"><svg width="24" height="20" viewBox="0 0 24 20" fill="var(--purple)"><path d="M0 20V10C0 4 3 1 9 0v4C6 5 5 7 5 10h4v10zM14 20V10c0-6 3-9 9-10v4c-3 1-4 3-4 6h4v10z"/></svg></div>
<p class="abs testi-text">Lorem Ipsum is simply dummy text of the printing and typesetting industry. Lorem Ipsum has been the industry's standard dummy text ever since the 1500s, when an unknown printer took a galley of type and scrambled it to make a type specimen book. It has survived not only five centuries, but also.</p>
<div class="abs testi-meta">
  <span style="display:flex;gap:6px;align-items:center"><svg width="14" height="14" viewBox="0 0 14 14" fill="none" stroke="var(--purple)" stroke-width="1.5"><rect x="1" y="2" width="12" height="11"/><path d="M1 5h12M4 0v3M10 0v3"/></svg>17 Dec, 2024</span>
  <span style="display:flex;gap:6px;align-items:center"><svg width="14" height="14" viewBox="0 0 14 14" fill="none" stroke="var(--purple)" stroke-width="1.5"><circle cx="7" cy="4" r="3"/><path d="M1 14c0-4 3-6 6-6s6 2 6 6"/></svg>Mara Ellison</span>
</div>
<div class="abs testi-dots"><span></span><span></span><span class="on"></span><span></span><span></span></div>

<section class="abs form-band" role="img" aria-label="Dark photo of an office workspace"></section>
<h2 class="abs section-title form-title">Get Started Form</h2>
<div class="abs field" style="top:3896px"><svg width="12" height="12" viewBox="0 0 12 12" fill="#999"><circle cx="6" cy="3" r="3"/><path d="M0 12c0-4 3-5 6-5s6 1 6 5z"/></svg>Name</div>
<div class="abs field" style="top:3946px"><svg width="12" height="12" viewBox="0 0 12 12" fill="none" stroke="#999"><rect x=".5" y="2" width="11" height="8"/><path d="M.5 2l5.5 5 5.5-5"/></svg>Email</div>
<div class="abs field" style="top:3996px"><svg width="12" height="12" viewBox="0 0 12 12" fill="#999"><path d="M2 0h3l1 3-2 1c1 2 2 3 4 4l1-2 3 1v3c0 1-1 2-2 2C5 12 0 7 0 2 0 1 1 0 2 0z"/></svg>Phone</div>
<div class="abs message">Message</div>
<div class="abs submit">SUBMIT</div>

<footer class="abs footer">
  <div class="abs foot-col" style="left:100px">
    <h4>Contact Info</h4>
    <div class="foot-label">CALL US</div>
    <div class="foot-line">(555) 418-2760</div>
    <div class="foot-line">hello@brindleecommerce.com</div>
    <div class="foot-label">ADDRESS</div>
    <div class="foot-line">2810 Harlow Lane, Suite 6,<br>Fenwick, Ohio 45010</div>
    <div class="socials"><span></span><span></span><span></span><span></span></div>
  </div>
  <div class="abs foot-col" style="left:350px">
    <h4>Quick Link</h4>
    <div class="quick">Pricing<br>About Us<br>Services<br>Contact Us</div>
  </div>
  <div class="abs map" role="img" aria-label="Street map showing the office location"></div>
</footer>
<div class="abs copyright">Copyright © 2024 Brindle Ecommerce. All Rights Reserved</div>

</body>
</html>
```